Brightleaf Oruma needs a new label design for our Kombucha range- 5 Flavours

We need a label design for our Kombucha range. We are looking for a new look that says quality, vibrant, modern, energetic. The design should draw from our brand identity and the Zanzibar landscape, while communicating internationally. We need a label that describes us and catches the consumer's eye as they scan the supermarket shelves.
Each label should have the same design foundation- with a slight difference in colour to reflect the Kombucha Flavour. Our flavours are: Classic, Ginger/Turmeric, Hibiscus, Cinammon/Clove and Lemongrass.
I have attached in order: our current label (all info on label will remain the same), screenshots from our brand book, some images of labels we love. Our kombucha is packed in glass bottles- it may be nice to play with clear cut outs that bring out the colour of the beverage within the label design.
Check us out on Instagram @brightleaforuma for the vibe

```html
<!DOCTYPE html>
<html lang="en">
<head>
<meta charset="utf-8">
<title>Brightleaf Oruma Kombucha – Classic label</title>
<link rel="stylesheet" href="https://fonts.googleapis.com/css2?family=Montserrat:wght@400;700;800&display=swap">
<style>
  :root {
    --backdrop: #ebebeb;
    --label-yellow-deep: #dcc21e;
    --label-yellow: #fde01a;
    --kombucha-green: #0d6b3a;
    --ink: #111111;
    --band-white: #ffffff;
  }
  * { box-sizing: border-box; margin: 0; padding: 0; }
  html, body {
    width: 1200px;
    height: 1200px;
    overflow: hidden;
    background: var(--backdrop);
    font-family: "Montserrat", sans-serif;
  }
  .label {
    position: absolute;
    left: 278px;
    top: 229px;
    width: 644px;
    height: 742px;
    background: linear-gradient(90deg, var(--label-yellow-deep) 0%, var(--label-yellow) 60%, var(--label-yellow) 100%);
    overflow: hidden;
  }
  .brand {
    position: absolute;
    left: 162px;
    top: 190px;
    width: 277px;
  }
  .brand-name {
    font-weight: 800;
    font-size: 25px;
    line-height: 1;
    letter-spacing: 0.3px;
    color: var(--ink);
    text-transform: uppercase;
    white-space: nowrap;
    text-align: center;
  }
  .brand-tagline {
    display: flex;
    justify-content: space-between;
    margin-top: 30px;
    width: 277px;
    font-weight: 700;
    font-size: 11px;
    line-height: 1;
    color: var(--ink);
    text-transform: uppercase;
  }
  .flavour-band {
    position: absolute;
    left: 0;
    top: 571px;
    width: 100%;
    height: 90px;
    background: var(--band-white);
    z-index: 1;
  }
  .product-name {
    position: absolute;
    left: 165px;
    top: 291px;
    font-weight: 800;
    font-size: 108px;
    line-height: 101px;
    letter-spacing: 0.5px;
    color: var(--kombucha-green);
    z-index: 2;
  }
  .product-name span { display: block; }
  .flavour-name {
    position: absolute;
    left: 180px;
    top: 612px;
    font-weight: 400;
    font-size: 38px;
    line-height: 1;
    letter-spacing: 1px;
    color: var(--ink);
    z-index: 2;
  }
  .badges {
    position: absolute;
    left: 0;
    top: 674px;
    width: 100%;
    height: 57px;
  }
  .badge { position: absolute; top: 0; }
  .badge-vegan { left: 153px; }
  .badge-organic { left: 450px; }
</style>
</head>
<body>
  <main class="label">
    <header class="brand">
      <h1 class="brand-name">Brightleaf Oruma</h1>
      <p class="brand-tagline"><span>Feed your body</span><span>Feed your mind</span></p>
    </header>

    <h2 class="product-name"><span>KOM</span><span>BU</span><span>CHA</span></h2>

    <div class="flavour-band"></div>
    <p class="flavour-name">CLASSIC</p>

    <div class="badges">
      <svg class="badge badge-vegan" width="57" height="57" viewBox="0 0 57 57" role="img" aria-label="Vegan certification badge">
        <circle cx="28.5" cy="28.5" r="26.5" fill="none" stroke="var(--kombucha-green)" stroke-width="2"/>
      </svg>
      <svg class="badge badge-organic" width="57" height="57" viewBox="0 0 57 57" role="img" aria-label="Organic certification badge">
        <circle cx="28.5" cy="28.5" r="26.5" fill="none" stroke="var(--kombucha-green)" stroke-width="2"/>
      </svg>
    </div>
  </main>
</body>
</html>
```